Frameless shower doors web site

Build a web site for information and display past projects. Contact information, type of work done. Customer Reviews. The design purpose is to generate phone calls and email inquirers. Domain name is Southernshowerdoors.comEmail is Brightpanelworks@mailbarn.com Profile We Love What We Do!Lakeview Bath Panels & Mirror LLC. is committed to excellence in every aspect of our business. We hold a standard of integrity bound by fairness, honesty, and personal responsibility. Our distinction is the quality of service and attention to detail we bring to each project. Above all, we listen to our clients input to provide several design options available from designer glass to hardware. We also service and repair existing shower and tub enclosure. Installation of customer purchased enclosure are available by appointment. and address any concerns.

Target Market(s)

25 to 55 residential customers

Number of Pages Required

4 page

Font styles to use
Sans Serif

Colors

Designer to choose colors to be used in the design.

Requirements
Nice to have
• Looking to drive phone calls for estimating shower projects
Should not have
• Lot of prescriptive words, Clutter

```html
<!DOCTYPE html>
<html lang="en">
<head>
<meta charset="utf-8">
<title>Lakeview Bath Panels &amp; Mirror</title>
<link rel="stylesheet" href="https://fonts.googleapis.com/css2?family=Exo+2:wght@600;700;800&family=Lato:wght@400;700;900&display=swap">
<style>
:root{
  --navy:#0f1d3d;
  --deep:#172a63;
  --blue:#1c5bc2;
  --bright:#1f86e6;
  --sky:#3d9bf2;
  --ink:#33405a;
  --white:#ffffff;
  --footer:#0d1730;
  --line:#2a3654;
  --muted:#b8c3d9;
}
*{box-sizing:border-box;margin:0;padding:0}
html,body{width:1200px;height:3529px;overflow:hidden}
body{position:relative;font-family:"Lato",sans-serif;color:var(--ink);background:var(--white)}
.abs{position:absolute}
.heading{font-family:"Exo 2",sans-serif;font-weight:800;letter-spacing:.5px}

/* header / hero */
.hero{left:0;top:0;width:1200px;height:741px;background:linear-gradient(120deg,#eef1f5 0%,#c9d1dc 35%,#aebac9 60%,#dde2ea 100%)}
.brand{left:141px;top:40px;display:flex;align-items:center;gap:12px;font-family:"Exo 2",sans-serif;font-weight:700;font-size:30px;color:var(--deep);line-height:1}
.brand-mark{width:22px;height:22px;background:var(--deep);flex:none}
.call{left:792px;top:22px;font-family:"Exo 2",sans-serif;font-weight:700;color:var(--blue);font-size:20px;display:flex;align-items:center;gap:8px}
.call strong{font-size:25px;color:var(--deep)}
.nav{left:433px;top:72px;display:flex;gap:31px;font-family:"Exo 2",sans-serif;font-weight:700;font-size:16px;color:var(--blue);text-transform:uppercase}
.hero-hex{left:110px;top:170px}
.hero-title{left:118px;top:350px;width:412px;text-align:center;color:var(--white);font-size:44px;line-height:48px}
.btn-solid{background:var(--navy);color:var(--white);font-family:"Exo 2",sans-serif;font-weight:700;font-size:19px;display:flex;align-items:center;justify-content:center}
.hero-btn{left:198px;top:463px;width:256px;height:50px}
.dots{left:562px;top:695px;display:flex;gap:8px}
.dots span{width:12px;height:12px;border-radius:50%;border:2px solid var(--white)}
.dots span.on{background:var(--white)}

/* about */
.section-title{font-size:42px;color:var(--deep)}
.about-title{left:160px;top:826px}
.copy{font-size:16.5px;line-height:27px;color:var(--deep)}
.about-p1{left:160px;top:898px;width:440px}
.about-p2{left:160px;top:966px;width:450px}
.btn-line{border:3px solid var(--blue);color:var(--blue);font-family:"Exo 2",sans-serif;font-weight:700;font-size:19px;display:flex;align-items:center;justify-content:center}
.about-btn{left:160px;top:1101px;width:193px;height:47px}
.about-hex{left:650px;top:680px}

/* services */
.services{left:0;top:1299px;width:1200px;height:631px;background:linear-gradient(115deg,#1d6fd6 0%,#2a7be0 40%,#1a4fae 75%,#223d8a 100%)}
.services-title{left:169px;top:1462px;color:var(--white);font-size:36px}
.services-copy{color:var(--white)}
.services-p1{left:172px;top:1517px;width:380px}
.services-p2{left:172px;top:1585px;width:380px}
.services-btn{left:174px;top:1750px;width:195px;height:50px;border-color:var(--white);color:var(--white)}
.card{width:231px;height:227px;color:var(--white);text-align:center;padding-top:20px}
.card svg{display:block;margin:0 auto 10px}
.card h3{font-family:"Exo 2",sans-serif;font-weight:700;font-size:15.5px;line-height:17px;text-transform:uppercase;margin-bottom:10px}
.card p{font-size:13px;line-height:19px;padding:0 30px}
.card-frameless{left:600px;top:1400px;background:var(--deep)}
.card-repair{left:849px;top:1351px;background:var(--navy)}
.card-tub{left:600px;top:1647px;background:var(--bright)}
.card-install{left:849px;top:1602px;background:var(--navy)}

/* doors */
.doors-title{left:0;top:1972px;width:1200px;text-align:center;font-size:36px}
.doors-grid{left:0;top:2030px}

/* inquiry */
.inquiry{left:0;top:2607px;width:1200px;height:511px;background:linear-gradient(160deg,#3b8fe8 0%,#2a7ce0 45%,#1d67cf 100%)}
.inquiry-notch{left:400px;top:2607px}
.inquiry-title{left:0;top:2672px;width:1200px;text-align:center;color:var(--white);font-size:33px}
.field{background:var(--white);font-size:15px;color:#667;padding:12px 20px;height:49px}
.f-name{left:186px;top:2744px;width:405px}
.f-phone{left:605px;top:2744px;width:407px}
.f-email{left:186px;top:2805px;width:405px}
.f-city{left:605px;top:2805px;width:407px}
.f-msg{left:186px;top:2866px;width:826px;height:82px}
.submit{left:501px;top:2974px;width:195px;height:52px}

/* footer */
.footer{left:0;top:3118px;width:1200px;height:411px;background:var(--footer)}
.foot-brand{left:150px;top:3240px;width:270px;color:var(--white);font-size:22px}
.foot-brand .brand-mark{background:var(--white);width:18px;height:18px}
.foot-head{font-family:"Lato",sans-serif;font-weight:900;font-size:17px;color:var(--white);text-transform:uppercase}
.fh-contact{left:452px;top:3208px}
.fh-company{left:697px;top:3208px}
.fh-touch{left:887px;top:3208px}
.foot-list{font-size:14px;color:var(--white);line-height:27px;list-style:none}
.fl-contact{left:452px;top:3252px;width:230px}
.fl-contact li{display:flex;gap:12px;align-items:flex-start;line-height:18px;margin-bottom:14px}
.fl-contact svg{flex:none}
.fl-company{left:700px;top:3248px}
.fl-touch{left:887px;top:3248px;line-height:34px}
.fl-touch li{display:flex;align-items:center;gap:10px}
.fl-touch i{width:24px;height:24px;border-radius:50%;background:var(--white);display:inline-block}
.foot-rule{left:0;top:3459px;width:1200px;height:1px;background:var(--line)}
.copyright{left:0;top:3481px;width:1200px;text-align:center;font-size:13.5px;color:var(--muted)}
</style>
</head>
<body>

<!-- Hero -->
<div class="abs hero" role="img" aria-label="Bright marble bathroom with a frameless glass walk-in shower"></div>
<div class="abs brand"><span class="brand-mark"></span>Lakeview Bath Panels</div>
<div class="abs call">
  <svg width="18" height="18" viewBox="0 0 24 24"><path d="M6.6 10.8a15.1 15.1 0 0 0 6.6 6.6l2.2-2.2c.3-.3.7-.4 1-.2 1.1.4 2.3.6 3.6.6.6 0 1 .4 1 1V20c0 .6-.4 1-1 1A17 17 0 0 1 3 4c0-.6.4-1 1-1h3.5c.6 0 1 .4 1 1 0 1.3.2 2.5.6 3.6.1.3 0 .7-.2 1z" fill="currentColor"/></svg>
  CALL US <strong>555 210 4471</strong>
</div>
<nav class="abs nav"><span>About</span><span>Services</span><span>Why Us</span><span>Testimonials</span><span>Door Design</span><span>Contact</span></nav>
<svg class="abs hero-hex" width="430" height="570" viewBox="0 0 430 570">
  <polygon points="215,4 424,128 424,442 215,566 6,442 6,128" fill="#1c5bc2" fill-opacity=".88" stroke="#1a4fae" stroke-width="6"/>
</svg>
<h1 class="abs hero-title heading">WE LOVE<br>WHAT WE DO!</h1>
<div class="abs btn-solid hero-btn">BOOK A APPOINTMENT</div>
<div class="abs dots"><span></span><span class="on"></span><span class="on"></span><span class="on"></span></div>

<!-- About -->
<h2 class="abs heading section-title about-title">ABOUT US</h2>
<p class="abs copy about-p1">Pellentesque faucibus Ut accumsan ultricies elit Maecenas at justo id velit placerat molestie Donec dictum</p>
<p class="abs copy about-p2">Mauris nunc quam venenatis nec euismod sit amet egestas placerat est Pellentesque habitant morbi tristique senectus et netus et malesuada fames ac turpis egestas Cras id elit Integer quis urna Ut ante enim dapibus malesuad</p>
<div class="abs btn-line about-btn">LEARN MORE</div>
<svg class="abs about-hex" width="430" height="560" viewBox="0 0 430 560">
  <defs><linearGradient id="aboutPhoto" x1="0" y1="0" x2="1" y2="1"><stop offset="0" stop-color="#d9dee5"/><stop offset=".55" stop-color="#9fadbd"/><stop offset="1" stop-color="#cfd6df"/></linearGradient></defs>
  <polyline points="60,82 215,2 370,82" fill="none" stroke="#1f86e6" stroke-width="5"/>
  <polyline points="60,478 215,558 370,478" fill="none" stroke="#1f86e6" stroke-width="5"/>
  <polygon points="215,30 404,140 404,420 215,530 26,420 26,140" fill="url(#aboutPhoto)" role="img" aria-label="Glass shower enclosure with tiled walls"/>
</svg>

<!-- Services -->
<div class="abs services" role="img" aria-label="Blue tinted bathroom background"></div>
<h2 class="abs heading services-title">OUR SERVICES</h2>
<p class="abs copy services-copy services-p1">Pellentesque faucibus Ut accumsan ultricies elit Maecenas at justo id velit placerat mo</p>
<p class="abs copy services-copy services-p2">Mauris nunc quam venenatis nec euismod sit amet egestas placerat est Pellentesque habitant morbi tristique senectus et netus et malesuada fames ac turpis egestas Cras id elit Integer quis urna Ut ante enim dapibus malesuad</p>
<div class="abs btn-line services-btn">LEARN MORE</div>

<div class="abs card card-frameless">
  <svg width="40" height="66" viewBox="0 0 40 66"><rect x="6" y="3" width="28" height="60" rx="2" fill="none" stroke="#fff" stroke-width="2.5"/><line x1="24" y1="26" x2="24" y2="38" stroke="#fff" stroke-width="2.5"/></svg>
  <h3>Frameless<br>Shower</h3>
  <p>Lorem ipsum dolor sit amet consectetuer adipisci</p>
</div>
<div class="abs card card-repair">
  <svg width="64" height="66" viewBox="0 0 64 66"><circle cx="32" cy="24" r="16" fill="none" stroke="#fff" stroke-width="2.5" stroke-dasharray="6 3"/><circle cx="32" cy="24" r="7" fill="none" stroke="#fff" stroke-width="2.5"/><path d="M6 50 q14 -6 26 2 h14 q6 0 10 -6 M6 62 h40 q8 0 12 -8" fill="none" stroke="#fff" stroke-width="2.5"/></svg>
  <h3>Repair<br>Existing Shower</h3>
  <p>Lorem ipsum dolor sit amet consectetuer adipisci</p>
</div>
<div class="abs card card-tub">
  <svg width="90" height="60" viewBox="0 0 90 60"><path d="M6 16 h78 q-4 36 -39 38 q-35 -2 -39 -38z" fill="none" stroke="#fff" stroke-width="2.5"/><path d="M18 22 h54 q-5 22 -27 24 q-22 -2 -27 -24z" fill="none" stroke="#fff" stroke-width="2"/></svg>
  <h3>Tub<br>Enclosure</h3>
  <p>Lorem ipsum dolor sit amet consectetuer adipisci</p>
</div>
<div class="abs card card-install">
  <svg width="66" height="66" viewBox="0 0 66 66"><path d="M10 56 L44 22 M40 12 a10 10 0 1 0 14 14 l-6 -2 -4 -4 z" fill="none" stroke="#fff" stroke-width="2.5"/><path d="M12 12 l8 0 36 36 -6 6 -36 -36z" fill="none" stroke="#fff" stroke-width="2.5"/></svg>
  <h3>Installation<br>of Purchased<br>Enclosure</h3>
  <p>Lorem ipsum dolor sit amet consectetuer adipisci</p>
</div>

<!-- Doors -->
<h2 class="abs heading section-title doors-title">OUR DOORS</h2>
<svg class="abs doors-grid" width="1200" height="580" viewBox="0 0 1200 580">
  <defs>
    <linearGradient id="doorA" x1="0" y1="0" x2="1" y2="1"><stop offset="0" stop-color="#6c7687"/><stop offset="1" stop-color="#333c4c"/></linearGradient>
    <linearGradient id="doorB" x1="0" y1="0" x2="1" y2="1"><stop offset="0" stop-color="#e4e8ec"/><stop offset="1" stop-color="#9ea9b6"/></linearGradient>
    <linearGradient id="doorC" x1="0" y1="0" x2="1" y2="1"><stop offset="0" stop-color="#c7ccd3"/><stop offset="1" stop-color="#7d8693"/></linearGradient>
    <linearGradient id="doorD" x1="0" y1="0" x2="1" y2="1"><stop offset="0" stop-color="#8a7e70"/><stop offset="1" stop-color="#3f3a36"/></linearGradient>
  </defs>
  <polygon role="img" aria-label="Dark bathroom vanity with glass shower" points="325,17 459,90 459,238 325,311 191,238 191,90" fill="url(#doorA)"/>
  <polygon role="img" aria-label="Frameless glass shower with white tiles" points="612,17 746,90 746,238 612,311 478,238 478,90" fill="url(#doorB)"/>
  <polygon role="img" aria-label="Grey marble walk-in shower" points="904,17 1038,90 1038,238 904,311 770,238 770,90" fill="url(#doorC)"/>
  <polygon role="img" aria-label="Marble shower niche with mosaic tile" points="466,264 600,337 600,497 466,570 332,497 332,337" fill="url(#doorB)"/>
  <polygon role="img" aria-label="Wood vanity and glass shower enclosure" points="755,264 889,337 889,497 755,570 621,497 621,337" fill="url(#doorD)"/>
  <circle cx="325" cy="165" r="28" fill="none" stroke="#fff" stroke-width="3"/>
  <circle cx="322" cy="162" r="9" fill="none" stroke="#fff" stroke-width="3"/>
  <line x1="329" y1="169" x2="336" y2="176" stroke="#fff" stroke-width="3"/>
</svg>

<!-- Inquiry -->
<div class="abs inquiry" role="img" aria-label="Blue tinted tiled shower background"></div>
<svg class="abs inquiry-notch" width="400" height="40" viewBox="0 0 400 40"><polygon points="0,0 400,0 200,40" fill="#ffffff"/></svg>
<h2 class="abs heading inquiry-title">EMAIL INQUIRY</h2>
<div class="abs field f-name">Your Name</div>
<div class="abs field f-phone">Phone</div>
<div class="abs field f-email">Email</div>
<div class="abs field f-city">City</div>
<div class="abs field f-msg">Message</div>
<div class="abs btn-solid submit">SUBMIT</div>

<!-- Footer -->
<div class="abs footer"></div>
<div class="abs brand foot-brand"><span class="brand-mark"></span>Lakeview Bath Panels</div>
<h4 class="abs foot-head fh-contact">Contact Us</h4>
<h4 class="abs foot-head fh-company">Company</h4>
<h4 class="abs foot-head fh-touch">Get In Touch</h4>
<ul class="abs foot-list fl-contact">
  <li><svg width="14" height="18" viewBox="0 0 14 18"><path d="M7 1a6 6 0 0 0-6 6c0 4.5 6 10 6 10s6-5.5 6-10a6 6 0 0 0-6-6z" fill="none" stroke="#fff" stroke-width="1.5"/><circle cx="7" cy="7" r="2" fill="#fff"/></svg><span>48 Harbor Lane Suite 3,<br>Austin TX 78701</span></li>
  <li><svg width="14" height="14" viewBox="0 0 24 24"><path d="M6.6 10.8a15.1 15.1 0 0 0 6.6 6.6l2.2-2.2c.3-.3.7-.4 1-.2 1.1.4 2.3.6 3.6.6.6 0 1 .4 1 1V20c0 .6-.4 1-1 1A17 17 0 0 1 3 4c0-.6.4-1 1-1h3.5c.6 0 1 .4 1 1 0 1.3.2 2.5.6 3.6.1.3 0 .7-.2 1z" fill="none" stroke="#fff" stroke-width="2"/></svg><span>555.302.7781</span></li>
  <li><svg width="16" height="12" viewBox="0 0 16 12"><rect x="1" y="1" width="14" height="10" fill="none" stroke="#fff" stroke-width="1.4"/><polyline points="1,1 8,7 15,1" fill="none" stroke="#fff" stroke-width="1.4"/></svg><span>hello@brightpanelworks.com</span></li>
</ul>
<ul class="abs foot-list fl-company"><li>Home</li><li>About us</li><li>Services</li><li>Our Doors</li><li>Contact</li></ul>
<ul class="abs foot-list fl-touch">
  <li><i></i>Chirpline</li><li><i></i>Facepage</li><li><i></i>Worknet</li><li><i></i>Snapgram</li>
</ul>
<div class="abs foot-rule"></div>
<p class="abs copyright">Copyright © 2019 All right reserved</p>

</body>
</html>
```